Quote Cards With TK May 2025 for Instagram

I would like to put these quotes over one of the pictures attached; Instagram (new size: 4:5 (1080 x 1350 pixels) One Quote per picture, and I want the quote to be bold or easy to read as well. I provided a few reference graphics that I really like as examples below. In very small letters at the bottom add @TKBarlowOnline

All of the pictures are attached; you can pick any photo and add one quote to it; but no stock photography

```html
<!DOCTYPE html>
<html lang="en">
<head>
<meta charset="utf-8">
<title>Quote Cards With TK – May 2025</title>
<link rel="stylesheet" href="https://fonts.googleapis.com/css2?family=Anton&family=Montserrat:wght@500&family=Roboto+Condensed:wght@700&family=Tinos:wght@400;700&family=Gelasio&family=Arimo:wght@700&family=Roboto+Slab:wght@700&display=swap">
<style>
  :root{
    --page:#ffffff;
    --ink:#111111;
    --white:#ffffff;
    --veil:rgba(205,205,200,.62);
    --dark-veil:rgba(34,32,30,.78);
    --gold-veil:rgba(200,162,40,.6);
    --brown-panel:#5e3d25;
    --handle:rgba(255,255,255,.88);
  }
  *{margin:0;padding:0;box-sizing:border-box}
  html,body{width:1200px;height:1200px;overflow:hidden;background:var(--page)}
  .sheet{position:relative;width:1200px;height:1200px}
  .card{position:absolute;width:274px;height:343px;overflow:hidden}
  .photo{position:absolute;inset:0}
  .handle{position:absolute;font-family:"Tinos",serif;font-size:7px;color:var(--handle)}
  .abs{position:absolute}

  /* card 1 – hillside */
  .c1{left:29px;top:30px}
  .c1 .photo{background:
    radial-gradient(ellipse 32% 60% at 50% 48%,rgba(20,20,22,.95) 0%,rgba(20,20,22,.85) 55%,rgba(20,20,22,0) 100%),
    radial-gradient(ellipse 40% 35% at 8% 85%,#3f5a2c 0%,rgba(63,90,44,0) 100%),
    radial-gradient(ellipse 35% 40% at 95% 75%,#4a6a34 0%,rgba(74,106,52,0) 100%),
    radial-gradient(ellipse 45% 25% at 15% 35%,#7a7560 0%,rgba(122,117,96,0) 100%),
    linear-gradient(180deg,#7d93a6 0%,#8c9aa2 22%,#6e7460 40%,#5b6848 60%,#3e4d30 100%)}
  .c1 .quote-box{left:34px;top:189px;width:206px;height:121px;background:var(--veil);padding:9px 9px;
    font-family:"Montserrat",sans-serif;font-size:14.3px;line-height:19.4px;letter-spacing:.9px;color:#1a1a1a;text-transform:uppercase;white-space:nowrap}
  .c1 .handle{left:34px;top:316px}

  /* card 2 – night window */
  .c2{left:321px;top:30px}
  .c2 .photo{background:
    radial-gradient(ellipse 26% 65% at 45% 50%,rgba(12,12,14,.95) 0%,rgba(12,12,14,.8) 60%,rgba(12,12,14,0) 100%),
    radial-gradient(ellipse 40% 45% at 75% 55%,#2b4aa0 0%,rgba(43,74,160,0) 100%),
    radial-gradient(ellipse 30% 30% at 72% 38%,#c8a060 0%,rgba(200,160,96,0) 100%),
    linear-gradient(90deg,#1a1a1c 0%,#2a2c34 30%,#1c2a5a 60%,#101a40 85%,#232020 100%)}
  .c2 .quote{left:0;right:0;top:146px;text-align:center;font-family:"Anton",sans-serif;font-size:21px;line-height:24.3px;color:var(--white);text-shadow:0 1px 3px rgba(0,0,0,.75);white-space:nowrap}
  .c2 .handle{left:0;right:0;top:271px;text-align:center}

  /* card 3 – white kitchen */
  .c3{left:612px;top:30px}
  .c3 .photo{background:
    radial-gradient(ellipse 30% 28% at 50% 32%,#1e1c1c 0%,rgba(30,28,28,0) 100%),
    radial-gradient(ellipse 38% 22% at 52% 50%,#f2f0ee 0%,rgba(242,240,238,0) 100%),
    radial-gradient(ellipse 30% 45% at 50% 85%,#1e1c1e 0%,rgba(30,28,30,0) 100%),
    linear-gradient(180deg,#f0f0f0 0%,#dedcda 45%,#9a9794 65%,#7a7674 100%)}
  .c3 .bar{left:22px;top:205px;width:240px;height:65px;background:var(--dark-veil)}
  .c3 .quote{left:29px;top:205px;font-family:"Montserrat",sans-serif;font-size:15.5px;line-height:21.3px;letter-spacing:.3px;color:var(--white);white-space:nowrap;text-transform:uppercase;text-shadow:0 1px 2px rgba(0,0,0,.5)}
  .c3 .handle{right:20px;top:311px}

  /* card 4 – stage */
  .c4{left:903px;top:30px}
  .c4 .photo{background:
    radial-gradient(ellipse 16% 55% at 52% 55%,#e23cb0 0%,rgba(226,60,176,.6) 55%,rgba(226,60,176,0) 100%),
    radial-gradient(ellipse 30% 25% at 40% 12%,#d48a40 0%,rgba(212,138,64,0) 100%),
    radial-gradient(ellipse 40% 40% at 15% 70%,#2a2a80 0%,rgba(42,42,128,0) 100%),
    linear-gradient(135deg,#3a2a8a 0%,#5a2f8f 40%,#7a2d90 60%,#2a2068 100%)}
  .c4 .ask{right:182px;top:152px;text-align:right;font-family:"Roboto Condensed",sans-serif;font-weight:700;font-size:15.5px;line-height:18px;color:var(--white);white-space:nowrap}
  .c4 .answer{left:170px;top:208px;font-family:"Roboto Condensed",sans-serif;font-weight:700;font-size:14.5px;line-height:17.5px;color:var(--white);white-space:nowrap}
  .c4 .cta{left:0;right:0;top:290px;text-align:center;font-family:"Arimo",sans-serif;font-weight:700;font-size:24px;color:var(--white)}
  .c4 .handle{right:10px;top:328px}

  /* card 5 – sunny apartment */
  .c5{left:31px;top:391px;width:272px;height:340px}
  .c5 .photo{background:
    radial-gradient(ellipse 30% 45% at 52% 45%,#2a2224 0%,rgba(42,34,36,.7) 55%,rgba(42,34,36,0) 100%),
    radial-gradient(ellipse 25% 30% at 88% 20%,#f0ece8 0%,rgba(240,236,232,0) 100%),
    linear-gradient(90deg,#3a3a44 0%,#6a6a70 12%,#c8c4c0 30%,#d8d4d0 70%,#bab6b2 100%)}
  .c5 .ask-box{left:32px;top:197px;width:207px;height:47px;background:#000;color:var(--white)}
  .c5 .cta-box{left:32px;top:244px;width:207px;height:69px;background:var(--white);color:var(--ink)}
  .c5 .ask-box,.c5 .cta-box{padding:0 7px;font-family:"Tinos",serif;font-size:19.5px;line-height:24px;white-space:nowrap}
  .c5 .handle{left:0;right:0;top:318px;text-align:center}

  /* card 6 – wood kitchen */
  .c6{left:322px;top:391px;width:273px;height:342px}
  .c6 .photo{background:
    radial-gradient(ellipse 45% 30% at 50% 50%,#18161a 0%,rgba(24,22,26,.8) 60%,rgba(24,22,26,0) 100%),
    radial-gradient(ellipse 14% 18% at 52% 30%,#1a1416 0%,rgba(26,20,22,0) 100%),
    linear-gradient(180deg,#6b4632 0%,#5a3a2a 40%,#8a7a6a 70%,#a09080 100%)}
  .c6 .quote-box{left:12px;top:202px;width:248px;height:123px;border:1px solid var(--white);background:rgba(190,185,180,.55);
    text-align:center;font-family:"Anton",sans-serif;font-size:19.5px;line-height:22.8px;color:var(--ink);padding-top:5px;white-space:nowrap}
  .c6 .handle{left:0;right:0;top:331px;text-align:center}

  /* card 7 – court */
  .c7{left:613px;top:391px;width:274px;height:342px}
  .c7 .panel{left:0;top:0;width:135px;height:100%;background:var(--brown-panel)}
  .c7 .photo{left:136px;background:
    radial-gradient(ellipse 28% 50% at 50% 55%,#1a1616 0%,rgba(26,22,22,.7) 55%,rgba(26,22,22,0) 100%),
    radial-gradient(ellipse 22% 18% at 48% 38%,#8a5a38 0%,rgba(138,90,56,0) 100%),
    linear-gradient(180deg,#1e2030 0%,#3a3040 20%,#c8b8a8 45%,#d8c0a0 65%,#e8b830 85%,#d8a020 100%)}
  .c7 .quote{left:10px;top:104px;font-family:"Anton",sans-serif;font-size:16px;line-height:20.2px;color:var(--white);white-space:nowrap}
  .c7 .handle{left:10px;top:323px}

  /* card 8 – shadowed room */
  .c8{left:903px;top:391px;width:275px;height:343px}
  .c8 .photo{background:
    radial-gradient(ellipse 28% 48% at 70% 55%,#161414 0%,rgba(22,20,20,.8) 60%,rgba(22,20,20,0) 100%),
    radial-gradient(ellipse 30% 30% at 60% 25%,#8a8678 0%,rgba(138,134,120,0) 100%),
    linear-gradient(90deg,#7a766a 0%,#6a665c 45%,#4a4640 75%,#1e1c1c 100%)}
  .c8 .intro{left:11px;top:164px;font-family:"Gelasio",serif;font-size:17.5px;line-height:21.5px;color:#1a1a1a;white-space:nowrap}
  .c8 .promise{left:6px;top:256px;width:159px;height:68px;border:1px solid #2a2a2a;background:rgba(150,145,130,.35);padding:1px 4px;
    font-family:"Gelasio",serif;font-size:17.5px;line-height:21.5px;color:#1a1a1a;white-space:nowrap}
  .c8 .handle{left:116px;top:330px}

  /* card 9 – sunflowers */
  .c9{left:321px;top:751px;width:274px;height:343px}
  .c9 .photo{background:
    radial-gradient(ellipse 24% 55% at 28% 50%,#a8707c 0%,rgba(168,112,124,.7) 55%,rgba(168,112,124,0) 100%),
    radial-gradient(ellipse 20% 45% at 82% 35%,#a87884 0%,rgba(168,120,132,0) 100%),
    radial-gradient(ellipse 60% 30% at 50% 90%,#c8a020 0%,rgba(200,160,32,0) 100%),
    linear-gradient(180deg,#8a8e90 0%,#b0a8a0 30%,#8a7040 60%,#6a5418 100%)}
  .c9 .quote-box{left:122px;top:140px;width:132px;height:106px;background:var(--gold-veil);padding:3px 6px;
    font-family:"Roboto Slab",serif;font-weight:700;font-size:12.5px;line-height:18.3px;letter-spacing:.4px;color:#1a1a1a;white-space:nowrap}
  .c9 .cta{left:123px;top:254px;font-family:"Roboto Slab",serif;font-weight:700;font-size:12.8px;line-height:18.5px;letter-spacing:.3px;color:var(--white);white-space:nowrap;text-shadow:0 1px 2px rgba(0,0,0,.55)}
  .c9 .handle{left:123px;top:296px}

  /* card 10 – golden backdrop */
  .c10{left:612px;top:751px;width:275px;height:343px}
  .c10 .photo{background:
    radial-gradient(ellipse 30% 55% at 32% 55%,#141212 0%,rgba(20,18,18,.75) 55%,rgba(20,18,18,0) 100%),
    radial-gradient(circle at 30% 20%,#f4d488 0%,#c7852e 45%,#4a2a18 100%)}
  .c10 .panel{left:126px;top:0;width:136px;height:100%;background:linear-gradient(180deg,#7a4530 0%,#c7a99a 45%,#b08878 75%,#7a4a38 100%)}
  .c10 .strip{left:262px;top:0;width:13px;height:100%;background:linear-gradient(180deg,#c79a50,#e8c880)}
  .c10 .quote{left:126px;width:136px;top:106px;text-align:center;font-family:"Tinos",serif;font-size:17px;line-height:18.3px;letter-spacing:.3px;color:#1a1a1a;white-space:nowrap}
  .c10 .handle{right:23px;top:330px;color:#3a2a20}
</style>
</head>
<body>
<main class="sheet">

  <section class="card c1">
    <div class="photo" role="img" aria-label="Woman in black top posing outdoors on hillside"></div>
    <p class="abs quote-box">Tired. Moody.<br>Stubborn belly fat.<br>Your hormones are<br>screaming for help!<br>Let's fix that.</p>
    <span class="handle">@TKBarlowOnline</span>
  </section>

  <section class="card c2">
    <div class="photo" role="img" aria-label="Woman in sheer black outfit before night city window"></div>
    <p class="abs quote">THAT STUBBORN WEIGHT?<br>IT'S NOT YOUR FAULT.<br>YOUR HORMONES ARE TO BLAME<br>AND YOU'RE NOT ALONE;<br>BUT THERE IS A FIX.</p>
    <span class="handle">@TKBarlowOnline</span>
  </section>

  <section class="card c3">
    <div class="photo" role="img" aria-label="Woman in white cropped sweater dancing in kitchen"></div>
    <div class="abs bar"></div>
    <p class="abs quote">Your belly isn't fat…<br>It's hormonal.<br>And here's how to fix it.<br>Comment hormones<br>if nothing is working.</p>
    <span class="handle">@TKBarlowOnline</span>
  </section>

  <section class="card c4">
    <div class="photo" role="img" aria-label="Woman in pink gown on stage with purple lights"></div>
    <p class="abs ask">The stubborn<br>belly fat<br>after 40?</p>
    <p class="abs answer">It's not<br>about calories;<br>it's about<br>your hormones.</p>
    <p class="abs cta">Here is the fix!</p>
    <span class="handle">@TKBarlowOnline</span>
  </section>

  <section class="card c5">
    <div class="photo" role="img" aria-label="Woman in sheer striped top in sunlit apartment"></div>
    <p class="abs ask-box">Flat tummy in your 40s?<br>It's still possible!</p>
    <p class="abs cta-box">Comment BYE BELLY<br>to get the 10 secrets<br>to a flatter tummy</p>
    <span class="handle">@TKBarlowOnline</span>
  </section>

  <section class="card c6">
    <div class="photo" role="img" aria-label="Woman in striped black top pointing down in kitchen"></div>
    <p class="abs quote-box">BLOATING. MUFFIN TOP.<br>PUFFY WAISTLINE.<br>YOUR BODY'S SCREAMING<br>FOR A DIFFERENT KIND OF FIX.<br>HERE IT IS...</p>
    <span class="handle">@TKBarlowOnline</span>
  </section>

  <section class="card c7">
    <div class="abs panel"></div>
    <div class="photo" role="img" aria-label="Woman in bronze top standing on basketball court"></div>
    <p class="abs quote">YOU'RE DOING<br>ALL THE<br>“RIGHT” THINGS,<br>BUT YOUR BELLY<br>WON'T GO DOWN?<br>HERE'S WHAT<br>YOU HAVEN'T TRIED.</p>
    <span class="handle">@TKBarlowOnline</span>
  </section>

  <section class="card c8">
    <div class="photo" role="img" aria-label="Woman in open-back black top in shadowed room"></div>
    <p class="abs intro">This 90-day<br>plan helped<br>women over<br>40 slim down,</p>
    <p class="abs promise">Get a tiny waist<br>and feel sexy again.<br>You're next.</p>
    <span class="handle">@TKBarlowOnline</span>
  </section>

  <section class="card c9">
    <div class="photo" role="img" aria-label="Woman in pink knit set among sunflowers and mirrors"></div>
    <p class="abs quote-box">This is the secret<br>women over 40<br>are using<br>to get snatched;<br>without starving.</p>
    <p class="abs cta">Comment SKINNY<br>to get the exact plan.</p>
    <span class="handle">@TKBarlowOnline</span>
  </section>

  <section class="card c10">
    <div class="photo" role="img" aria-label="Woman in black outfit against golden backdrop"></div>
    <div class="abs panel"></div>
    <div class="abs strip"></div>
    <p class="abs quote">What worked<br>in your 30s<br>won't work now.<br>Here's what<br>actually does.<br>Drop 30 Pounds<br>in 3 Months.</p>
    <span class="handle">@TKBarlowOnline</span>
  </section>

</main>
</body>
</html>
```